cookie box packaging sleeve design

Hi,
I'm looking to create 5 sleeves for cookies in a box.
Classic look, not too many colors. I need to be able to add the nutrition info for each sleeve at the back.
width 110 mm height 370mm

1. Salted Tahini Choc-Chip Cookie
2. Brownie White Choc Cookie
3. Peanut Butter Cookie
4. Earthquake Cookie
5.Pistachio Cookie

ideas:
Biscotti by Brellanti (https://ryde.brellanti.example/?welcomed)
OR
https://au.snapvorra.example/pin/4830195726104388/

Target Market(s)

Family, office and for gifts

Industry/Entity Type

Cafe/Bakery

Colors

Designer to choose colors to be used in the design.

Requirements
Should not have
• Too many colours and the photo of the cookies

```html
<!DOCTYPE html>
<html lang="en">
<head>
<meta charset="utf-8">
<title>Tollenby House – Salted Tahini Choc-Chip Cookie Sleeve</title>
<link href="https://fonts.googleapis.com/css2?family=Alfa+Slab+One&family=Yellowtail&display=swap" rel="stylesheet">
<style>
  :root {
    --page: #ffffff;
    --sleeve-blue: #9dbbd0;
    --ink-blue: #a7c6dd;
    --label-white: #fdfdfd;
    --shadow: rgba(60, 90, 115, 0.12);
  }
  * { margin: 0; padding: 0; box-sizing: border-box; }
  html, body {
    width: 1200px;
    height: 675px;
    overflow: hidden;
    background: var(--page);
  }
  .canvas {
    width: 1200px;
    height: 675px;
    display: flex;
    align-items: center;
    justify-content: center;
  }
  .sleeve {
    position: relative;
    width: 196px;
    height: 640px;
    background: var(--sleeve-blue);
    box-shadow: 0 4px 18px var(--shadow);
    display: flex;
    flex-direction: column;
    align-items: center;
  }
  .sleeve__top-band { height: 176px; width: 100%; }
  .label {
    position: relative;
    width: 176px;
    background: var(--label-white);
    text-align: center;
    color: var(--ink-blue);
    font-family: "Alfa Slab One", serif;
  }
  .label--top { height: 148px; padding-top: 16px; }
  .label--front { height: 230px; padding-top: 36px; }
  .scallop-top::before,
  .scallop-bottom::after {
    content: "";
    position: absolute;
    left: 0;
    width: 100%;
    height: 6px;
    background: radial-gradient(circle at 5px 6px, var(--label-white) 4.5px, transparent 5px) repeat-x;
    background-size: 10px 6px;
  }
  .scallop-top::before { top: -6px; }
  .scallop-bottom::after {
    bottom: -6px;
    background: radial-gradient(circle at 5px 0, var(--label-white) 4.5px, transparent 5px) repeat-x;
    background-size: 10px 6px;
  }
  .label__gap { height: 60px; width: 100%; }
  .brand-name {
    font-size: 15px;
    letter-spacing: 0.5px;
    line-height: 1;
    margin-bottom: 10px;
  }
  .product-name {
    font-size: 12.5px;
    line-height: 1.08;
    letter-spacing: 0.6px;
  }
  .claim-ribbon {
    display: inline-block;
    margin-top: 6px;
    padding: 1px 8px;
    background: var(--ink-blue);
    color: var(--label-white);
    font-size: 5px;
    letter-spacing: 0.8px;
  }
  .tagline {
    margin-top: 5px;
    font-family: "Yellowtail", cursive;
    font-size: 9.5px;
    line-height: 1.1;
  }
  .net-weight {
    margin-top: 6px;
    font-size: 6px;
    letter-spacing: 1px;
  }
</style>
</head>
<body>
<main class="canvas">
  <section class="sleeve" aria-label="Cookie box sleeve">
    <div class="sleeve__top-band"></div>

    <div class="label label--top scallop-top">
      <p class="brand-name">Tollenby House</p>
      <h2 class="product-name">SALTED TAHINI<br>CHOC-CHIP COOKIE</h2>
      <p class="claim-ribbon">GLUTEN FREE &amp; DAIRY BISCUITS</p>
      <p class="tagline">Tradutional Italian Flourless almonds biscuits</p>
    </div>

    <div class="label label--front scallop-bottom">
      <p class="brand-name">Tollenby House</p>
      <h1 class="product-name">SALTED TAHINI<br>CHOC-CHIP COOKIE</h1>
      <p class="claim-ribbon">GLUTEN FREE &amp; DAIRY BISCUITS</p>
      <p class="net-weight">300G</p>
    </div>

    <div class="label__gap"></div>
  </section>
</main>
</body>
</html>
```